Business Card Design

We develop / design / build affordable housing throughout the state of Illinois.

Target Market(s)

non profit organizations and other developers / professionals in my industry

Industry/Entity Type

Business

Contact Information for Business Card

Verdell Ridge Construction, LLC
General Contracting
Marisol K Thornbury, CEO
418 North Wendell P Ashcroft Avenue, Suite 307
Elmhurst, IL 60126
630-555-0148
mkt@buildverdellridge.com

```html
<!DOCTYPE html>
<html lang="en">
<head>
<meta charset="utf-8">
<title>Verdell Ridge Construction – Business Card</title>
<link rel="stylesheet" href="https://fonts.googleapis.com/css2?family=Playfair+Display+SC:wght@400;700&family=Playfair+Display:wght@700&display=swap">
<style>
  :root {
    --paper: #ffffff;
    --band: #bfa894;
    --brown: #5a3a1c;
    --ink: #111111;
  }
  * { margin: 0; padding: 0; box-sizing: border-box; }
  html, body { width: 927px; height: 1200px; overflow: hidden; background: var(--paper); }
  .sheet { position: relative; width: 927px; height: 1200px; background: var(--paper); color: var(--ink); }

  .band { position: absolute; left: 55px; width: 818px; background: var(--band); }
  .band--top { top: 74px; height: 90px; }
  .band--contact { top: 506px; height: 90px; }
  .band--back-top { top: 638px; height: 88px; }
  .band--back-bottom { top: 1051px; height: 88px; }

  .brand-mark { position: absolute; left: 50%; width: 56px; height: 56px; margin-left: -28px; background: var(--brown); }
  .brand-mark--front { top: 262px; }
  .brand-mark--back { top: 862px; }

  .company-name {
    position: absolute; left: 0; right: 0; text-align: center;
    font-family: "Playfair Display SC", "Times New Roman", serif;
    font-weight: 700; font-size: 46px; letter-spacing: -0.5px; color: var(--ink);
  }
  .company-name--front { top: 330px; }
  .company-name--back { top: 928px; }

  .tagline {
    position: absolute; top: 386px; left: 0; right: 0; text-align: center;
    font-family: "Playfair Display SC", "Times New Roman", serif;
    font-size: 28px; letter-spacing: 1px; line-height: 1;
  }
  .person {
    position: absolute; top: 424px; left: 0; right: 0; text-align: center;
    font-family: "Playfair Display SC", "Times New Roman", serif;
    font-size: 20px; letter-spacing: 0.5px; line-height: 1;
  }

  .address {
    position: absolute; top: 520px; left: 64px;
    font-family: "Playfair Display SC", "Times New Roman", serif;
    font-size: 21px; line-height: 25px;
  }
  .contact {
    position: absolute; top: 525px; right: 79px; text-align: right;
    font-family: "Playfair Display", "Times New Roman", serif;
    font-weight: 700; font-size: 21px; line-height: 24px;
  }
</style>
</head>
<body>
<main class="sheet">
  <div class="band band--top"></div>

  <section class="card-front">
    <div class="brand-mark brand-mark--front"></div>
    <h1 class="company-name company-name--front">Verdell Ridge Construction</h1>
    <p class="tagline">LLC General Contracting</p>
    <p class="person">Marisol K Thornbury, CEO</p>
  </section>

  <div class="band band--contact"></div>
  <address class="address">418 North Wendell P Ashcroft Ave<br>Suite 307 Elmhurst, IL 60126</address>
  <p class="contact">(630) 555-0148<br>mkt@buildverdellridge.com</p>

  <div class="band band--back-top"></div>

  <section class="card-back">
    <div class="brand-mark brand-mark--back"></div>
    <p class="company-name company-name--back">Verdell Ridge Construction</p>
  </section>

  <div class="band band--back-bottom"></div>
</main>
</body>
</html>
```